Design 2 Print Banners for Conference Booth

We need a tall banner and a table banner rough designed for our Conference Booth. The link shows the current booth and what details for banner dimensions and text
see complete design brief here .. https://files.brindlepaper.net/doc/7QkTzR2mWpXa9LcVn4HsJd8EyBfU3oGtKiN6/view?mode=shared

Target Market(s)

Doctors & Medical Professionals

Industry/Entity Type

Google

Colors
33a6d7
cee9f5
ecf7fb

Requirements
Must have
• match our branding colors - see current booth backdrop and our website quietoaktesting.com

```html
<!DOCTYPE html>
<html lang="en">
<head>
<meta charset="utf-8">
<title>Quiet Oak Testing – Booth Banner</title>
<link rel="stylesheet" href="https://fonts.googleapis.com/css2?family=Roboto+Condensed:wght@300;400&display=swap">
<style>
  :root {
    --brand-blue: #33a6d7;
    --brand-deep: #1d6e93;
    --tint-mid: #cee9f5;
    --tint-light: #ecf7fb;
    --text-grey: #4a4a4a;
    --meadow-glow: #f4f08a;
    --meadow-yellow: #d9d52a;
    --meadow-lime: #a9c52a;
    --meadow-green: #5e8f1e;
    --meadow-shade: #2b3a16;
  }
  html, body {
    margin: 0;
    padding: 0;
    width: 1200px;
    height: 2523px;
    overflow: hidden;
    background: var(--tint-light);
  }
  .banner {
    position: relative;
    width: 1200px;
    height: 2523px;
    background: var(--tint-light);
    font-family: "Roboto Condensed", Arial, sans-serif;
    color: var(--text-grey);
    overflow: hidden;
  }

  /* brand */
  .brand {
    position: absolute;
    top: 120px;
    left: 0;
    width: 1200px;
    display: flex;
    align-items: center;
    justify-content: center;
    gap: 30px;
  }
  .brand-dot {
    width: 104px;
    height: 104px;
    border-radius: 50%;
    background: var(--brand-blue);
    flex: none;
  }
  .brand-name {
    font-size: 100px;
    font-weight: 400;
    color: var(--brand-deep);
    line-height: 1;
  }

  /* testimonial */
  .testimonial {
    position: absolute;
    top: 520px;
    left: 150px;
    width: 900px;
    margin: 0;
  }
  .testimonial-quote {
    margin: 0;
    text-align: center;
    font-size: 64px;
    font-weight: 300;
    line-height: 84px;
  }
  .testimonial-author {
    display: block;
    text-align: right;
    margin-top: 20px;
    padding-right: 58px;
    font-size: 38px;
    font-weight: 300;
  }

  /* call to action */
  .cta {
    position: absolute;
    top: 1070px;
    left: 0;
    width: 1200px;
    text-align: center;
  }
  .cta-lead {
    margin: 0;
    font-size: 62px;
    font-weight: 300;
    line-height: 1;
  }
  .cta-action {
    margin: 50px 0 0;
    font-size: 90px;
    font-weight: 300;
    line-height: 1;
    color: var(--brand-deep);
  }

  /* meadow area */
  .hero-art {
    position: absolute;
    left: 0;
    top: 0;
    width: 1200px;
    height: 2523px;
  }
  .accent-band { fill: var(--brand-blue); }
  .stop-glow { stop-color: var(--meadow-glow); }
  .stop-yellow { stop-color: var(--meadow-yellow); }
  .stop-lime { stop-color: var(--meadow-lime); }
  .stop-green { stop-color: var(--meadow-green); }
  .stop-shade { stop-color: var(--meadow-shade); }
</style>
</head>
<body>
<main class="banner">
  <svg class="hero-art" viewBox="0 0 1200 2523" width="1200" height="2523">
    <defs>
      <radialGradient id="meadow-light" cx="1" cy="0.05" r="1.15">
        <stop class="stop-glow" offset="0"/>
        <stop class="stop-yellow" offset="0.28"/>
        <stop class="stop-lime" offset="0.55"/>
        <stop class="stop-green" offset="0.8"/>
        <stop class="stop-shade" offset="1"/>
      </radialGradient>
    </defs>
    <path class="accent-band" d="M0 1965 Q 430 1400 1200 1413 L1200 2523 L0 2523 Z"/>
    <path class="meadow-photo" role="img"
          aria-label="Photo of a relaxed man lying in a sunny meadow of grass and yellow dandelions"
          d="M0 2000 Q 440 1505 1200 1515 L1200 2523 L0 2523 Z" fill="url(#meadow-light)"/>
  </svg>

  <header class="brand">
    <span class="brand-dot"></span>
    <span class="brand-name">Quiet Oak Testing</span>
  </header>

  <figure class="testimonial">
    <blockquote class="testimonial-quote">"No single endeavour has had<br>as great a financial impact<br>on our practice as choosing to<br>work with Quiet Oak Testing"</blockquote>
    <figcaption class="testimonial-author">- Dana Whitlow</figcaption>
  </figure>

  <section class="cta">
    <p class="cta-lead">Get The Facts Instantly</p>
    <p class="cta-action">Text ALLERGY to 52720</p>
  </section>
</main>
</body>
</html>
```